Postcard for Antique Furniture Restorer

My business is to restore antique furniture. I am based in Sydney, Australia.

I will be using this postcard to promote my business.
I will give it to customers like a With Compliments card.

Sometimes I will be writing information on the back of the card.

Design for Postcard Size eg 148 X 105mm

Front of card:

Attached are images of Antique furniture - please use ONLY 1 of the 3 images.
Deep etch the image on a white or cream background.

On front of card add these words:
Timber Awakened
antique furniture restoration

Antiques travel through time, seeing generations of families
Through time they remain - they tell a continuing story
Be part of the journey

Back of postcard:
(leave space for notes to be handwritten)

Add these words:

Timber Awakened
Corwin Aldace
mobile 0437 552 681
www.oakmendworks.com.au

Industry/Entity Type

Business

Font styles to use
Serif
Sans Serif

Colors
fefdec
ffffff

Requirements
Must have
• Use only 1 image. Image must be deep etched.

```html
<!DOCTYPE html>
<html lang="en">
<head>
<meta charset="utf-8">
<title>Timber Awakened – Postcard</title>
<link rel="stylesheet" href="https://fonts.googleapis.com/css2?family=Archivo+Black&family=Josefin+Sans:wght@300;400;700&display=swap">
<style>
  :root {
    --page: #e7e7e7;
    --card: #f7f5d9;
    --card-light: #fefdec;
    --ink: #1f1f1f;
    --ink-soft: #3a3a3a;
    --chest-dark: #6e3218;
    --chest-mid: #8d4a26;
    --chest-light: #a5603a;
  }
  * { box-sizing: border-box; margin: 0; padding: 0; }
  html, body { width: 894px; height: 1200px; overflow: hidden; }
  body {
    background: var(--page);
    font-family: "Josefin Sans", sans-serif;
    color: var(--ink);
    position: relative;
  }

  /* 148 × 105 mm postcard ratio */
  .card {
    position: absolute;
    left: 77px;
    width: 740px;
    height: 525px;
    background: radial-gradient(ellipse at 50% 35%, var(--card-light), var(--card) 75%);
    box-shadow: 0 6px 18px rgba(0,0,0,0.18);
  }
  .card--front { top: 45px; }
  .card--back { top: 630px; }

  .brand { position: absolute; left: 0; right: 0; text-align: center; }
  .brand__name {
    font-family: "Archivo Black", sans-serif;
    font-weight: 400;
    font-size: 38px;
    letter-spacing: 5px;
    line-height: 1;
    text-transform: uppercase;
    color: var(--ink);
  }
  .brand__tagline {
    font-weight: 300;
    font-size: 16px;
    line-height: 20px;
    color: var(--ink-soft);
  }
  .card--front .brand { top: 26px; }
  .card--back .brand { top: 70px; }

  .photo {
    position: absolute;
    top: 104px;
    left: 215px;
    width: 310px;
    height: 232px;
    border-radius: 4px;
    background: linear-gradient(180deg, var(--chest-light) 0%, var(--chest-mid) 45%, var(--chest-dark) 100%);
  }

  .story {
    position: absolute;
    top: 356px; left: 0; right: 0;
    text-align: center;
    font-weight: 300;
    font-size: 19px;
    line-height: 28px;
    color: var(--ink);
  }
  .story__call { font-weight: 700; }

  .contact { display: flex; align-items: center; gap: 6px; font-weight: 400; color: var(--ink); }
  .contact svg { width: 15px; height: 15px; fill: var(--ink); flex: none; }

  .footer {
    position: absolute;
    top: 478px; left: 40px; right: 40px;
    display: flex;
    justify-content: space-between;
    font-size: 14px;
  }

  .contact-block {
    position: absolute;
    top: 250px; left: 240px;
    font-size: 18px;
    line-height: 24px;
  }
  .contact-block .contact svg { width: 16px; height: 16px; }
</style>
</head>
<body>

<section class="card card--front">
  <header class="brand">
    <h1 class="brand__name">Timber Awakened</h1>
    <p class="brand__tagline">antique furniture restoration</p>
  </header>

  <div class="photo" role="img" aria-label="Deep-etched photograph of a restored mahogany chest of drawers with brass handles"></div>

  <div class="story">
    <p>Antiques travel through time, seeing generations of families</p>
    <p>Through time they remain - they tell a continuing story</p>
    <p class="story__call">Be part of the journey</p>
  </div>

  <footer class="footer">
    <span class="contact">
      <svg viewBox="0 0 16 16" aria-hidden="true"><circle cx="8" cy="4.5" r="3.5"/><path d="M1 16c0-4 3-6.5 7-6.5s7 2.5 7 6.5z"/></svg>
      Corwin Aldace
    </span>
    <span class="contact">
      <svg viewBox="0 0 16 16" aria-hidden="true"><path d="M1 6c0-2 3-3.5 7-3.5S15 4 15 6v1.5h-3.5V6h-7v1.5H1z"/><path d="M3.5 8h9l1.5 6H2z"/><circle cx="8" cy="11" r="1.6" fill="#f7f5d9"/></svg>
      0437 552 681
    </span>
    <span class="contact">
      <svg viewBox="0 0 16 16" aria-hidden="true"><path d="M8 1a7 7 0 1 0 0 14A7 7 0 0 0 8 1zm5.4 6h-2.5a11 11 0 0 0-1-4.3A5.5 5.5 0 0 1 13.4 7zM8 2.6c.7.9 1.3 2.5 1.4 4.4H6.6C6.7 5.1 7.3 3.5 8 2.6zM6.1 2.7A11 11 0 0 0 5.1 7H2.6a5.5 5.5 0 0 1 3.5-4.3zM2.6 8.5h2.5a11 11 0 0 0 1 4.3 5.5 5.5 0 0 1-3.5-4.3zM8 13.4c-.7-.9-1.3-2.5-1.4-4.9h2.8c-.1 2.4-.7 4-1.4 4.9zm1.9-.1a11 11 0 0 0 1-4.8h2.5a5.5 5.5 0 0 1-3.5 4.8z"/></svg>
      www.oakmendworks.com.au
    </span>
  </footer>
</section>

<section class="card card--back">
  <header class="brand">
    <h2 class="brand__name">Timber Awakened</h2>
    <p class="brand__tagline">antique furniture restoration</p>
  </header>

  <div class="contact-block">
    <p class="contact">
      <svg viewBox="0 0 16 16" aria-hidden="true"><circle cx="8" cy="4.5" r="3.5"/><path d="M1 16c0-4 3-6.5 7-6.5s7 2.5 7 6.5z"/></svg>
      Corwin Aldace
    </p>
    <p class="contact">
      <svg viewBox="0 0 16 16" aria-hidden="true"><path d="M1 6c0-2 3-3.5 7-3.5S15 4 15 6v1.5h-3.5V6h-7v1.5H1z"/><path d="M3.5 8h9l1.5 6H2z"/><circle cx="8" cy="11" r="1.6" fill="#f7f5d9"/></svg>
      0437 552 681
    </p>
    <p class="contact">
      <svg viewBox="0 0 16 16" aria-hidden="true"><path d="M8 1a7 7 0 1 0 0 14A7 7 0 0 0 8 1zm5.4 6h-2.5a11 11 0 0 0-1-4.3A5.5 5.5 0 0 1 13.4 7zM8 2.6c.7.9 1.3 2.5 1.4 4.4H6.6C6.7 5.1 7.3 3.5 8 2.6zM6.1 2.7A11 11 0 0 0 5.1 7H2.6a5.5 5.5 0 0 1 3.5-4.3zM2.6 8.5h2.5a11 11 0 0 0 1 4.3 5.5 5.5 0 0 1-3.5-4.3zM8 13.4c-.7-.9-1.3-2.5-1.4-4.9h2.8c-.1 2.4-.7 4-1.4 4.9zm1.9-.1a11 11 0 0 0 1-4.8h2.5a5.5 5.5 0 0 1-3.5 4.8z"/></svg>
      www.oakmendworks.com.au
    </p>
  </div>
</section>

</body>
</html>
```